Beer labels for RQ Craft Brews Range

Labels for RQ Craft Brews trademark beer range.

We are a new craft beer brewery and we have developed our 4 trademark beers and we are looking for label for each beer. The labels will have to have some brand recognition between them, so that a beer lover can see it’s a RQ Craft Brew on the shelf.

Each label will need to have the name and type, imagery associated with the name, company logo (supplied), alcohol percentage, grain ingredients, hop ingredients, place for the story of the beer, volume of can/bottle (330 ml with the average fill e mark) and a place for the IBU and EBC info about the beer. We are open to total creativity.

We don’t want something too busy and loud. We have color ideas for each, but we are happy to see other colors that the designers think work better. We also like the idea of icons to highlight sections – but we are not tied to this. Something that looks great and professional is what we are after.

We need two label sizes; 9 cm (h) x 20.5 cm (w) and 9 cm (h) x 18.5 cm (w) for all four labels. All the space is available for design. We would like to see all 4 designs in a mockup on 330 ml bottle and cans.

The four beers that we need labels for are:

1. Juniper Evenings
o This is a New England IPA and the inspiration around this beer is our time living in North Carolina. The imagery we want on this beer is North Carolina related. Mountain, trees etc.
o 6.7% vol.
o IBU = 9 and EBC = 11
o Grains: Pale Malt, Wheat Malt and Flaked Oats
o Hops: Chinook, Quintaro, Brenlow, Velka and Tundrel
o We would like the Latin quote Esse Quam Videri on the label somewhere, it plays on our story and concept
o Pastel green

2. Valen
o This is a Porter and the inspiration around the North East of Scotland. The imagery we what on this beer is North East Scotland; something like a stag. But open to ideas.
o 5.3% vol.
o IBU = 39 and EBC = 240
o Grains: Pale Malt, Black Malt, Roast Wheat Malt and Chocolate Malt
o Hops: Fuggles, Challenger and Quintaro
o Grey

3. Maisie’s
o This is an American Pale Ale and the inspiration for this beer is one of the founder’s dog. She is a lovely Golden Retriever we would like the imagery to be golden retriever based.
o 5.5% vol.
o IBU = 3 and EBC = 13
o Grains: Pale Malt and Munich Malt
o Hops: Quintaro, Brenlow and Velka
o Golden

4. Bolt Upright
o This is a Pilsner Beer and the inspiration for this beer is the country of Czech Republic, the home of the Pilsner. The imagery to be about the Czech Republic (flag country shape, Prague etc.)
o 4.5% vol.
o IBU = 23 and EBC = 8
o Grains: Pilsner Malt, Amber Malt and Dornamalt Malt
o Hops: Saaz
o Blue

Suggest submitting one label as an example of what your ideas are like. Look forward to seeing what you do :)

Added some inspiration labels

Craft Beer drinkers

• Each label will need to have the name and type, imagery associated with the name, company logo (supplied; preferable so it is visible on shelf), alcohol percentage, grain ingredients, hop ingredients, place for the story of the beer, volume of can/bottle (330 ml with the average fill e mark) and a place for the IBU and EBC info about the beer.

```html
<!DOCTYPE html>
<html lang="en">
<head>
<meta charset="utf-8">
<title>RQ Craft Brews – Valen Porter Label</title>
<link rel="stylesheet" href="https://fonts.googleapis.com/css2?family=Roboto+Condensed:wght@400;700&display=swap">
<style>
  :root {
    --sky-lilac: #b49ab8;
    --sky-mist: #d4c6d8;
    --sky-pale: #dfe3ea;
    --abv-red: #e2574c;
    --ink: #2a2226;
    --ink-soft: #4a3f46;
    --brand-red: #d8453c;
    --card: #f5f3f4;
    --band-light: #e9a9b1;
    --band-pink: #cf7f8b;
    --band-ink: #3a2a30;
    --page: #f4f1f3;
  }
  html, body {
    margin: 0;
    padding: 0;
    width: 800px;
    height: 1200px;
    overflow: hidden;
    background: var(--page);
  }
  .label {
    position: relative;
    width: 800px;
    height: 1200px;
    overflow: hidden;
    font-family: "Roboto Condensed", "Arial Narrow", sans-serif;
    color: var(--ink);
  }
  .label__sky {
    position: absolute;
    inset: 0 0 185px 0;
    background: linear-gradient(180deg,
      var(--sky-lilac) 0%,
      var(--sky-mist) 42%,
      #cfc3d6 58%,
      var(--sky-pale) 78%,
      #e6e4ea 100%);
  }

  /* Title */
  .title {
    position: absolute;
    left: 40px;
    top: 60px;
    margin: 0;
  }
  .title__name {
    display: block;
    font-size: 150px;
    font-weight: 700;
    line-height: 1;
    letter-spacing: 4px;
    text-transform: uppercase;
  }
  .title__type {
    display: block;
    margin-top: 8px;
    font-size: 40px;
    font-weight: 400;
    letter-spacing: 10px;
    text-transform: uppercase;
    color: var(--ink-soft);
  }

  /* Info columns */
  .info {
    position: absolute;
    left: 40px;
    top: 330px;
    width: 720px;
    display: grid;
    grid-template-columns: 320px 360px;
    column-gap: 40px;
  }
  .info__heading {
    margin: 0 0 6px;
    font-size: 22px;
    font-weight: 700;
    letter-spacing: 3px;
    text-transform: uppercase;
    color: var(--brand-red);
  }
  .info__list {
    margin: 0 0 22px;
    font-size: 22px;
    line-height: 1.35;
  }
  .info__story {
    margin: 0;
    font-size: 21px;
    line-height: 1.45;
    color: var(--ink-soft);
  }

  /* ABV badge */
  .abv {
    position: absolute;
    left: 40px;
    top: 600px;
    width: 140px;
    height: 140px;
    border-radius: 50%;
    background: var(--abv-red);
    display: flex;
    align-items: center;
    justify-content: center;
  }
  .abv__value {
    margin: 0;
    font-size: 44px;
    font-weight: 700;
    letter-spacing: 0.5px;
  }

  /* Imagery */
  .imagery {
    position: absolute;
    left: 320px;
    top: 600px;
    width: 440px;
    height: 290px;
    background: linear-gradient(180deg, #c9bfd0 0%, #8f8590 55%, #3e3438 100%);
  }

  /* Brand */
  .brand {
    position: absolute;
    left: 24px;
    top: 790px;
    width: 256px;
    height: 80px;
    box-sizing: border-box;
    border: 4px solid var(--brand-red);
    background: var(--card);
    display: flex;
    align-items: center;
    justify-content: center;
    gap: 12px;
  }
  .brand__mark {
    width: 18px;
    height: 18px;
    background: var(--brand-red);
  }
  .brand__name {
    margin: 0;
    font-size: 30px;
    font-weight: 700;
    color: var(--brand-red);
  }

  /* Stats */
  .stats {
    position: absolute;
    left: 320px;
    top: 915px;
    width: 440px;
    display: flex;
    justify-content: space-between;
  }
  .stat {
    margin: 0;
    font-size: 26px;
    font-weight: 700;
    letter-spacing: 2px;
  }
  .stat__label {
    font-weight: 400;
    color: var(--ink-soft);
  }

  /* Bottom bands */
  .label__band-top {
    position: absolute;
    left: 0;
    right: 0;
    bottom: 152px;
    height: 33px;
    background: var(--band-light);
  }
  .label__band {
    position: absolute;
    left: 0;
    right: 0;
    bottom: 0;
    height: 152px;
    background: var(--band-pink);
  }
  .volume {
    position: absolute;
    right: 40px;
    bottom: 56px;
    margin: 0;
    font-size: 36px;
    font-weight: 700;
    color: var(--band-ink);
  }
</style>
</head>
<body>
  <main class="label">
    <div class="label__sky" role="img" aria-label="Painted lilac sky with soft clouds over misty hills and speckled texture"></div>

    <h1 class="title">
      <span class="title__name">Valen</span>
      <span class="title__type">Porter</span>
    </h1>

    <section class="info">
      <div class="info__ingredients">
        <h2 class="info__heading">Grains</h2>
        <p class="info__list">Pale Malt, Black Malt, Roast Wheat Malt, Chocolate Malt</p>
        <h2 class="info__heading">Hops</h2>
        <p class="info__list">Fuggles, Challenger, Quintaro</p>
      </div>
      <div class="info__about">
        <h2 class="info__heading">Our Story</h2>
        <p class="info__story">Brewed in memory of misty mornings across the North East of Scotland, where stags roam the heather and dark roasted malt warms cold evenings.</p>
      </div>
    </section>

    <div class="abv"><p class="abv__value">5.3%</p></div>

    <div class="imagery" role="img" aria-label="Painted stag standing on a dark hillside under a lilac sky"></div>

    <div class="brand">
      <span class="brand__mark" aria-hidden="true"></span>
      <p class="brand__name">RQ Craft Brews</p>
    </div>

    <div class="stats">
      <p class="stat"><span class="stat__label">IBU</span> 39</p>
      <p class="stat"><span class="stat__label">EBC</span> 240</p>
      <p class="stat"><span class="stat__label">ABV</span> 5.3%</p>
    </div>

    <div class="label__band-top"></div>
    <div class="label__band" role="img" aria-label="Pink band with dark halftone dot pattern"></div>
    <p class="volume">330 ml ℮</p>
  </main>
</body>
</html>
```